We would like to incorporate our logo into letterhead design and envelopes. We are looking for something that is moderately conservative but not old law firm style. Both the envelopes and the letterhead must have both firm addresses. We would like to incorporate the color of the logo, but only a small amount of color - perhaps on one of the borders. The addresses for the firm locations are listed below. Given that it is a law firm, it needs to somewhat conservative, but not the old school, small black font on cream colored paper design.

The firm addresses are:

27815 N. Harlow Pemberton Pkwy.
Ste 4200
Scottsdale, AZ 85391

6100 W. Cedar Avenue
Ste 700
Burbank, CA 91623

Industry/Entity Type

Legal

Colors

Designer to choose colors to be used in the design.

Requirements
Must have
• Both addresses:
• 27815 N. Harlow Pemberton Pkwy.
• Ste 4200
• Scottsdale, AZ 85391
• 6100 W. Cedar Avenue
• Ste 700
• Burbank, CA 91623
Nice to have
• Small amount of color on border(s) that matches the logo but not too much color

```html
<!DOCTYPE html>
<html lang="en">
<head>
<meta charset="utf-8">
<title>Calloway Law — Letterhead and Envelope</title>
<link rel="stylesheet" href="https://fonts.googleapis.com/css2?family=Arimo:wght@400&display=swap">
<style>
  :root {
    --ink: #484690;
    --paper: #ffffff;
    --backdrop: #e7e7eb;
    --edge: rgba(0, 0, 0, 0.18);
  }
  html, body {
    margin: 0;
    padding: 0;
    width: 960px;
    height: 1200px;
    overflow: hidden;
    background: var(--backdrop);
  }
  .stationery {
    position: relative;
    width: 960px;
    height: 1200px;
    font-family: "Arimo", Arial, sans-serif;
  }
  .sheet {
    position: absolute;
    background: var(--paper);
    box-shadow: 0 4px 14px var(--edge);
  }
  .sheet svg { display: block; width: 100%; height: 100%; }
  .letterhead { left: 100px; top: 40px; width: 840px; height: 1087px; }
  .envelope { left: 20px; top: 500px; width: 820px; height: 356px; }
  .firm-name { fill: var(--ink); font-family: "Arimo", Arial, sans-serif; font-weight: 400; }
  .address { fill: var(--ink); font-family: "Arimo", Arial, sans-serif; }
  .frame, .rule { stroke: var(--ink); fill: none; }
</style>
</head>
<body>
<main class="stationery">

  <section class="sheet letterhead" aria-label="Letterhead">
    <svg viewBox="0 0 840 1087" xmlns="http://www.w3.org/2000/svg">
      <text class="firm-name" x="55" y="150" font-size="44" textLength="365" lengthAdjust="spacingAndGlyphs">CALLOWAY LAW</text>

      <polyline class="frame" stroke-width="5" points="445,105 790,105 790,985 620,985"/>
      <polyline class="frame" stroke-width="1.5" points="450,118 777,118 777,972 620,972"/>

      <g class="address" font-size="18" text-anchor="end">
        <text x="325" y="878">27815 N. Harlow Pemberton Pkwy.</text>
        <text x="325" y="904">Ste 4200</text>
        <text x="325" y="930">Scottsdale, AZ 85391</text>
      </g>
      <g class="rules">
        <line class="rule" x1="40" y1="945" x2="330" y2="945" stroke-width="1"/>
        <line class="rule" x1="40" y1="958" x2="330" y2="958" stroke-width="2"/>
        <line class="rule" x1="40" y1="972" x2="330" y2="972" stroke-width="3"/>
        <line class="rule" x1="40" y1="990" x2="330" y2="990" stroke-width="7"/>
      </g>
      <g class="address" font-size="18">
        <text x="345" y="958">6100 W. Cedar Avenue</text>
        <text x="345" y="984">Ste 700</text>
        <text x="345" y="1010">Burbank, CA 91623</text>
      </g>
    </svg>
  </section>

  <section class="sheet envelope" aria-label="Envelope">
    <svg viewBox="0 0 820 356" xmlns="http://www.w3.org/2000/svg">
      <text class="firm-name" x="60" y="110" font-size="38" textLength="315" lengthAdjust="spacingAndGlyphs">CALLOWAY LAW</text>

      <polyline class="frame" stroke-width="5" points="400,60 760,60 760,290 630,290"/>
      <polyline class="frame" stroke-width="1.5" points="405,72 748,72 748,278 630,278"/>

      <g class="address" font-size="15" text-anchor="end">
        <text x="330" y="190">27815 N. Harlow Pemberton Pkwy.</text>
        <text x="330" y="212">Ste 4200</text>
        <text x="330" y="234">Scottsdale, AZ 85391</text>
      </g>
      <g class="rules">
        <line class="rule" x1="40" y1="246" x2="335" y2="246" stroke-width="1"/>
        <line class="rule" x1="40" y1="257" x2="335" y2="257" stroke-width="2"/>
        <line class="rule" x1="40" y1="269" x2="335" y2="269" stroke-width="3"/>
        <line class="rule" x1="40" y1="285" x2="335" y2="285" stroke-width="6"/>
      </g>
      <g class="address" font-size="15">
        <text x="345" y="257">6100 W. Cedar Avenue</text>
        <text x="345" y="279">Ste 700</text>
        <text x="345" y="301">Burbank, CA 91623</text>
      </g>
    </svg>
  </section>

</main>
</body>
</html>
```